Broschüre in Querformat für Immobilienmakler
Zielgruppe
Immobilienmakler - Überregional tätig - zielgerichtete Vermarktung - Zielgruppe sind Verkäufer oft ältere Menschen
Ich möchte eine Broschüre mit 12 Seiten im Querformat - Die Broschüre sollte der Website harvrenk-immobilien.example ein wenig ähneln.
Aufgabenstellung
klare Linie - schnell erklärbar und übersichtlich - logischer Aufbau - Aufmerksamkeit erwecken durch Bilder - schnelle Info für Querleser - VERTRAUEN - ehrlich und authentisch - nicht Eitel - schnelle Zurechtfindung - Serviceorientiert - Rundumsorglos Paket

```html
<!DOCTYPE html>
<html lang="de">
<head>
<meta charset="utf-8">
<title>Checkliste Immobilienverkauf – Broschüre Seiten 05/06</title>
<link rel="stylesheet" href="https://fonts.googleapis.com/css2?family=Open+Sans:wght@400;600&display=swap">
<style>
  :root {
    --stage: #d9d9db;
    --paper: #ffffff;
    --paper-shade: #f3f3f4;
    --brand-blue: #2a7fbc;
    --band-blue: #4a9fd0;
    --text-grey: #4a4a4a;
    --text-soft: #6b6b6b;
    --skyline-dark: #a3a3a3;
    --skyline-light: #ececec;
  }
  * { box-sizing: border-box; margin: 0; padding: 0; }
  html, body {
    width: 1200px; height: 769px; overflow: hidden;
    background: var(--stage);
    font-family: "Open Sans", Arial, sans-serif;
  }
  .spread {
    position: absolute; left: 40px; top: 182px;
    width: 1120px; height: 396px;
    display: flex;
    box-shadow: 0 14px 30px rgba(0,0,0,0.18);
  }
  .page {
    position: relative; width: 560px; height: 396px;
    background: var(--paper); overflow: hidden;
  }
  .page--left { background: linear-gradient(90deg, var(--paper) 85%, var(--paper-shade)); }
  .page--right { background: linear-gradient(90deg, var(--paper-shade), var(--paper) 12%); }
  .page-number {
    position: absolute; top: 14px; font-size: 9px; color: var(--band-blue); z-index: 2;
  }
  .page--left .page-number { right: 24px; }
  .page--right .page-number { right: 20px; color: #fff; top: 12px; }

  .cover-photo {
    position: absolute; left: 0; top: 0; width: 210px; height: 100%;
    background: linear-gradient(180deg, #3c6a8f 0%, #8d7f70 28%, #c98a4e 38%, #3b3a3c 55%, #262528 100%);
  }
  .skyline {
    position: absolute; bottom: 0; height: 56px; z-index: 1;
    background: linear-gradient(180deg, rgba(255,255,255,0) 0%, var(--skyline-light) 45%, var(--skyline-dark) 100%);
  }
  .page--left .skyline { left: 210px; right: 0; }
  .page--right .skyline { left: 0; right: 0; height: 90px; }

  .checklist-title {
    position: absolute; left: 232px; top: 34px; z-index: 2;
    color: var(--brand-blue); font-weight: 600; font-size: 19px; line-height: 1.15;
  }
  .documents {
    position: absolute; left: 232px; top: 88px; list-style: none; z-index: 2;
  }
  .documents li {
    display: flex; align-items: center; gap: 9px;
    font-size: 10.5px; color: var(--text-grey); height: 16px;
  }
  .tick { width: 12px; height: 12px; flex: none; }

  .title-band {
    position: absolute; left: 0; top: 0; width: 100%; height: 34px;
  }
  .title-band__label {
    position: absolute; left: 14px; top: 8px; color: #fff;
    font-size: 13px; font-weight: 600; z-index: 2;
  }
  .services {
    position: absolute; left: 30px; top: 50px; list-style: none; z-index: 2;
  }
  .services li {
    position: relative; padding-left: 18px;
    font-size: 9.5px; color: var(--text-soft); line-height: 16px;
  }
  .services li::before {
    content: ""; position: absolute; left: 0; top: 5px;
    width: 6px; height: 6px; border-radius: 50%; background: var(--brand-blue);
  }
  .services li.cont::before { display: none; }
</style>
</head>
<body>
  <main class="spread">
    <section class="page page--left">
      <div class="cover-photo" role="img" aria-label="Foto einer Großstadt-Skyline mit Hochhäusern bei Sonnenuntergang"></div>
      <span class="page-number">05</span>
      <h1 class="checklist-title">Checkliste Immobilienverkauf –<br>Unterlagen</h1>
      <ul class="documents">
        <li><svg class="tick" viewBox="0 0 12 12"><circle cx="6" cy="6" r="5.2" fill="none" stroke="var(--brand-blue)" stroke-width="1.1"/><path d="M3.5 6.2 5.3 7.9 8.6 4.4" fill="none" stroke="var(--brand-blue)" stroke-width="1.2"/></svg>Grundrisse</li>
        <li><svg class="tick" viewBox="0 0 12 12"><circle cx="6" cy="6" r="5.2" fill="none" stroke="var(--brand-blue)" stroke-width="1.1"/><path d="M3.5 6.2 5.3 7.9 8.6 4.4" fill="none" stroke="var(--brand-blue)" stroke-width="1.2"/></svg>Schnitt und Ansichten</li>
        <li><svg class="tick" viewBox="0 0 12 12"><circle cx="6" cy="6" r="5.2" fill="none" stroke="var(--brand-blue)" stroke-width="1.1"/><path d="M3.5 6.2 5.3 7.9 8.6 4.4" fill="none" stroke="var(--brand-blue)" stroke-width="1.2"/></svg>Wohnflächenberechnung</li>
        <li><svg class="tick" viewBox="0 0 12 12"><circle cx="6" cy="6" r="5.2" fill="none" stroke="var(--brand-blue)" stroke-width="1.1"/><path d="M3.5 6.2 5.3 7.9 8.6 4.4" fill="none" stroke="var(--brand-blue)" stroke-width="1.2"/></svg>Berechnung umbauter Raum m³</li>
        <li><svg class="tick" viewBox="0 0 12 12"><circle cx="6" cy="6" r="5.2" fill="none" stroke="var(--brand-blue)" stroke-width="1.1"/><path d="M3.5 6.2 5.3 7.9 8.6 4.4" fill="none" stroke="var(--brand-blue)" stroke-width="1.2"/></svg>Grundbuchauszug</li>
        <li><svg class="tick" viewBox="0 0 12 12"><circle cx="6" cy="6" r="5.2" fill="none" stroke="var(--brand-blue)" stroke-width="1.1"/><path d="M3.5 6.2 5.3 7.9 8.6 4.4" fill="none" stroke="var(--brand-blue)" stroke-width="1.2"/></svg>Liegenschaftskarte</li>
        <li><svg class="tick" viewBox="0 0 12 12"><circle cx="6" cy="6" r="5.2" fill="none" stroke="var(--brand-blue)" stroke-width="1.1"/><path d="M3.5 6.2 5.3 7.9 8.6 4.4" fill="none" stroke="var(--brand-blue)" stroke-width="1.2"/></svg>Nachweis einer Versicherung (Feuer)</li>
        <li><svg class="tick" viewBox="0 0 12 12"><circle cx="6" cy="6" r="5.2" fill="none" stroke="var(--brand-blue)" stroke-width="1.1"/><path d="M3.5 6.2 5.3 7.9 8.6 4.4" fill="none" stroke="var(--brand-blue)" stroke-width="1.2"/></svg>Personalausweis Verkäufer</li>
        <li><svg class="tick" viewBox="0 0 12 12"><circle cx="6" cy="6" r="5.2" fill="none" stroke="var(--brand-blue)" stroke-width="1.1"/><path d="M3.5 6.2 5.3 7.9 8.6 4.4" fill="none" stroke="var(--brand-blue)" stroke-width="1.2"/></svg>Baubeschreibung</li>
        <li><svg class="tick" viewBox="0 0 12 12"><circle cx="6" cy="6" r="5.2" fill="none" stroke="var(--brand-blue)" stroke-width="1.1"/><path d="M3.5 6.2 5.3 7.9 8.6 4.4" fill="none" stroke="var(--brand-blue)" stroke-width="1.2"/></svg>Energiekosten der letzten 3 Jahre</li>
        <li><svg class="tick" viewBox="0 0 12 12"><circle cx="6" cy="6" r="5.2" fill="none" stroke="var(--brand-blue)" stroke-width="1.1"/><path d="M3.5 6.2 5.3 7.9 8.6 4.4" fill="none" stroke="var(--brand-blue)" stroke-width="1.2"/></svg>Teilungserklärung</li>
        <li><svg class="tick" viewBox="0 0 12 12"><circle cx="6" cy="6" r="5.2" fill="none" stroke="var(--brand-blue)" stroke-width="1.1"/><path d="M3.5 6.2 5.3 7.9 8.6 4.4" fill="none" stroke="var(--brand-blue)" stroke-width="1.2"/></svg>Mietverträge</li>
        <li><svg class="tick" viewBox="0 0 12 12"><circle cx="6" cy="6" r="5.2" fill="none" stroke="var(--brand-blue)" stroke-width="1.1"/><path d="M3.5 6.2 5.3 7.9 8.6 4.4" fill="none" stroke="var(--brand-blue)" stroke-width="1.2"/></svg>Wirtschaftspläne 3 Jahre</li>
        <li><svg class="tick" viewBox="0 0 12 12"><circle cx="6" cy="6" r="5.2" fill="none" stroke="var(--brand-blue)" stroke-width="1.1"/><path d="M3.5 6.2 5.3 7.9 8.6 4.4" fill="none" stroke="var(--brand-blue)" stroke-width="1.2"/></svg>Hausgeldabrechnungen 3 Jahre</li>
        <li><svg class="tick" viewBox="0 0 12 12"><circle cx="6" cy="6" r="5.2" fill="none" stroke="var(--brand-blue)" stroke-width="1.1"/><path d="M3.5 6.2 5.3 7.9 8.6 4.4" fill="none" stroke="var(--brand-blue)" stroke-width="1.2"/></svg>Renovierungen der letzten 20 Jahre</li>
      </ul>
      <div class="skyline" role="img" aria-label="Grau gezeichnete Stadtsilhouette am unteren Seitenrand"></div>
    </section>

    <section class="page page--right">
      <svg class="title-band" viewBox="0 0 560 34" preserveAspectRatio="none" aria-hidden="true">
        <polygon points="0,12 270,12 282,0 560,0 560,8 284,8 270,22 0,22" fill="var(--band-blue)"/>
        <polygon points="0,8 272,8 260,30 0,30" fill="var(--brand-blue)"/>
      </svg>
      <span class="title-band__label">Checkliste Immobilienverkauf</span>
      <span class="page-number">06</span>
      <ul class="services">
        <li>Realistische Wertermittlung, basierend auf Marktanalyse und vergleichbaren Angeboten</li>
        <li>Zielgruppenanalyse zur Ermittlung passender Käufer</li>
        <li>Stärken/Schwächen-Analyse zur optimalen Aufbereitung und Präsentation der Immobilie</li>
        <li>Professionelle Exposéerstellung mit aussagekräftigen Fotos, Texten, Grundrissplänen</li>
        <li>Vermarktung in den großen Internetportalen, auf der Homepage, in Printmedien und direkt am</li>
        <li class="cont">Verkaufsobjekt</li>
        <li>Open-House Veranstaltungen (offene Besichtigung)</li>
        <li>Durchführung von Gemeinschaftsgeschäften mit Maklerkollegen aus dem bestehenden</li>
        <li class="cont">Netzwerkpartnern</li>
        <li>Bonitätsprüfung vom Kaufinteressenten</li>
        <li>Besichtigung mit „geprüften“ Interessenten</li>
        <li>Professionelle Preisverhandlungen</li>
        <li>Bankenunabhängige Finanzierungsberatung und Übernahme der gesamten Abwicklung</li>
        <li>Vorbereitung des Notarvertrages sowie Begleitung und Betreuung beim Notartermin</li>
        <li>After-Sales Service</li>
      </ul>
      <div class="skyline" role="img" aria-label="Grau gezeichnete Stadtsilhouette am unteren Seitenrand"></div>
    </section>
  </main>
</body>
</html>
```